Brightwell Electrical and Air conditioning services needs Designer Van Signage.

Brightwell Electrical and Air conditioning company needs a Van signage designed to give customers a professional image of the business. Attached are some sample design that we will be interested in. Do not need full van wrap, Back Half should be ok.

Industry/Entity Type

Electrical, Air conditioning, & Plumbing

Requirements
Must have
• 24 hour emergency service. Electrical , Air conditioning & Plumbing ideas. Please show all around van. front back and 2 sides.
Nice to have
• Please use mobile number: 0437205816, email: info@brightwellelectrical-example.com.au, Web: www.brightwellelectrical-example.com.au.
Should not have
• Full van wrap

```html
<!DOCTYPE html>
<html lang="en">
<head>
<meta charset="utf-8">
<title>Brightwell Van Signage</title>
<link rel="stylesheet" href="https://fonts.googleapis.com/css2?family=Poppins:wght@600&family=Montserrat:ital,wght@0,500;0,600;0,700;0,800;1,800&display=swap">
<style>
  :root {
    --orange: #e8893a;
    --blue: #1f5aa6;
    --red: #d8262b;
    --white: #ffffff;
    --page: #f1f1f1;
  }
  * { box-sizing: border-box; margin: 0; padding: 0; }
  html, body { width: 1200px; height: 1200px; overflow: hidden; }
  body {
    background: var(--page);
    font-family: "Montserrat", sans-serif;
    position: relative;
  }
  .panel {
    position: absolute;
    background: var(--white);
    overflow: hidden;
    box-shadow: 0 6px 18px rgba(0,0,0,0.10);
  }
  .panel-shapes { position: absolute; inset: 0; }
  .abs { position: absolute; white-space: nowrap; }

  .wordmark {
    font-family: "Poppins", sans-serif;
    font-weight: 600;
    color: var(--orange);
    line-height: 1;
    letter-spacing: -1px;
  }
  .services { font-weight: 700; line-height: 1; }
  .services .electrical { color: var(--red); }
  .services .aircon { color: var(--blue); margin: 0 0.5em; }
  .services .plumbing { color: var(--orange); }

  /* Side panel */
  .side-panel { left: 50px; top: 80px; width: 1100px; height: 440px; border-radius: 28px; }
  .side-panel .badge { left: 560px; top: 42px; text-align: center; }
  .badge-hours {
    font-weight: 800; font-style: italic; color: var(--blue);
    font-size: 54px; line-height: 1; display: flex; align-items: center; gap: 4px;
  }
  .badge-hours .slash { color: var(--red); }
  .badge-label {
    font-weight: 800; font-style: italic; font-size: 20px; line-height: 1.1;
  }
  .badge-label .l1 { color: var(--blue); display: block; }
  .badge-label .l2 { color: var(--red); display: block; padding-left: 30px; }
  .side-panel .phone {
    left: 88px; top: 190px; font-size: 20px; font-weight: 700;
    color: var(--blue); letter-spacing: 3px;
  }
  .side-panel .wordmark { left: 300px; top: 178px; font-size: 100px; }
  .side-panel .services { left: 306px; top: 300px; font-size: 22px; }
  .side-panel .web {
    left: 230px; width: 580px; top: 364px; text-align: center;
    font-size: 16px; font-weight: 500;
    color: var(--white); letter-spacing: 1.5px;
  }

  /* Front panel */
  .front-panel { left: 80px; top: 670px; width: 495px; height: 445px; border-radius: 22px; }
  .front-panel .wordmark { left: 0; right: 0; top: 180px; text-align: center; font-size: 52px; }
  .front-panel .services { left: 0; right: 0; top: 244px; text-align: center; font-size: 12px; }

  /* Back panel */
  .back-panel { left: 630px; top: 670px; width: 495px; height: 445px; border-radius: 22px; }
  .back-panel .wordmark { left: 0; right: 0; top: 48px; text-align: center; font-size: 50px; }
  .back-panel .services { left: 0; right: 0; top: 110px; text-align: center; font-size: 12.5px; }
  .back-panel .phone {
    left: 22px; top: 160px; font-size: 21px; font-weight: 800;
    color: var(--white); letter-spacing: 1.5px;
  }
  .back-panel .web {
    right: 20px; top: 166px; font-size: 11px; font-weight: 600; color: var(--white);
  }
  .back-panel .ghost-name {
    left: 0; right: 0; top: 225px; text-align: center; font-size: 96px;
    color: rgba(255,255,255,0.10);
  }
  .back-panel .emergency { left: 170px; top: 360px; display: flex; align-items: center; gap: 8px; }
  .back-panel .emergency-label {
    font-weight: 800; font-style: italic; font-size: 15px; color: var(--white);
    line-height: 1.1; text-align: right;
  }
  .back-panel .emergency-hours {
    font-weight: 800; font-style: italic; font-size: 38px; color: var(--white); line-height: 1;
  }
</style>
</head>
<body>

  <section class="panel side-panel" aria-label="Van side signage">
    <svg class="panel-shapes" viewBox="0 0 1100 440" aria-hidden="true">
      <path d="M840 0 H1100 V270 H930 Q860 220 850 120 Q845 50 840 0 Z" fill="var(--orange)"/>
      <path d="M720 400 Q760 300 900 280 Q1000 268 1100 272 V440 H720 Z" fill="var(--blue)"/>
      <path d="M210 352 H830 Q800 380 790 408 H220 Q205 380 210 352 Z" fill="var(--red)"/>
    </svg>

    <div class="abs badge">
      <div class="badge-hours">
        <span>24</span><span class="slash">/</span><span>7</span>
        <svg width="40" height="40" viewBox="0 0 40 40" aria-hidden="true">
          <circle cx="20" cy="20" r="16" fill="none" stroke="var(--orange)" stroke-width="3"/>
          <path d="M20 10 V20 L27 24" fill="none" stroke="var(--orange)" stroke-width="3" stroke-linecap="round"/>
        </svg>
      </div>
      <div class="badge-label"><span class="l1">Emergency</span><span class="l2">Services</span></div>
    </div>

    <div class="abs phone">0437205816</div>
    <div class="abs wordmark">Brightwell</div>
    <div class="abs services">
      <span class="electrical">Electrical</span><span class="aircon">Air Conditioning</span><span class="plumbing">Plumbing</span>
    </div>
    <div class="abs web">www.brightwellelectrical-example.com.au</div>
  </section>

  <section class="panel front-panel" aria-label="Van front signage">
    <div class="abs wordmark">Brightwell</div>
    <div class="abs services">
      <span class="electrical">Electrical</span><span class="aircon">Air Conditioning</span><span class="plumbing">Plumbing</span>
    </div>
  </section>

  <section class="panel back-panel" aria-label="Van rear signage">
    <svg class="panel-shapes" viewBox="0 0 495 445" aria-hidden="true">
      <rect x="0" y="150" width="495" height="45" fill="var(--red)"/>
      <rect x="0" y="195" width="495" height="16" fill="var(--orange)"/>
      <rect x="0" y="211" width="495" height="234" fill="var(--blue)"/>
    </svg>
    <div class="abs wordmark">Brightwell</div>
    <div class="abs services">
      <span class="electrical">Electrical</span><span class="aircon">Air Conditioning</span><span class="plumbing">Plumbing</span>
    </div>
    <div class="abs phone">0437205816</div>
    <div class="abs web">www.brightwellelectrical-example.com.au</div>
    <div class="abs wordmark ghost-name" aria-hidden="true">Brightwell</div>
    <div class="abs emergency">
      <div class="emergency-label">Emergency<br>Services</div>
      <div class="emergency-hours">24/7</div>
      <svg width="30" height="30" viewBox="0 0 40 40" aria-hidden="true">
        <circle cx="20" cy="20" r="16" fill="none" stroke="var(--white)" stroke-width="3"/>
        <path d="M20 10 V20 L27 24" fill="none" stroke="var(--white)" stroke-width="3" stroke-linecap="round"/>
      </svg>
    </div>
  </section>

</body>
</html>
```